Luxury travel agency needs a website design

We are a travel agency specializing in booking luxury vacations. We specialize in Hawaii, Europe and Caribbean, but will do all vacations. I want a very classy website design which would attract luxury clients. The company name is "Harbors and Hammocks Travel Agency". Would love the web design to go with the color scheme of the logo. Hex codes included in files. Logo is attached. Would also love more Grey in the website. I want it very elegant

Coding

Coded - Design and coding required

Font styles to use
Sans Serif
Decorative

Requirements
Must have
• - Consultation Tab or a page where the client can fill out a short form about what vacation that they would want to book. I want this info to be sent to me in order for me to contact them.
- Somewhere with my contact info "email: marla@harborsandhammockstravel.example and phone number"
- Social media links
- About section "Marla Denholm - Agency Owner (picture provided)
Marla has been traveling full time for the passed two years and has been very passionate about travel from a young age. Marla is dedicated to working closely with clients to book their dream vacation.
Marla's specializations include honeymoons and anniversaries focusing on travel in Europe, Hawaii and all inclusive resorts in the Caribbean.

```html
<!DOCTYPE html>
<html lang="en">
<head>
<meta charset="utf-8">
<title>Harbors and Hammocks Travel Agency</title>
<link href="https://fonts.googleapis.com/css2?family=Open+Sans:wght@400;600;700&family=Rye&display=swap" rel="stylesheet">
<style>
:root{
  --orange:#f0874a;
  --peach:#fde3d3;
  --grey-bg:#efefef;
  --ink:#2b2627;
  --text:#333333;
  --muted:#7a7a7a;
  --white:#ffffff;
  --sans:'Open Sans', Arial, sans-serif;
  --deco:'Rye', serif;
}
*{box-sizing:border-box;margin:0;padding:0}
html,body{width:1200px;height:4438px;overflow:hidden}
body{position:relative;background:var(--white);font-family:var(--sans);color:var(--text)}
.abs{position:absolute}

/* top bar + nav */
.topbar{top:0;left:0;width:1200px;height:41px;background:var(--orange);color:var(--white);font-size:14px;font-weight:600}
.topbar span{position:absolute;top:11px;display:flex;align-items:center;gap:7px;white-space:nowrap}
.nav{top:41px;left:0;width:1200px;height:74px;background:var(--white);border-bottom:4px solid var(--orange)}
.nav a{position:absolute;top:31px;font-size:14px;font-weight:700;color:var(--text);text-decoration:none;letter-spacing:.5px}
.nav a.active{color:var(--orange)}
.nav a.active::after{content:"";position:absolute;left:50%;bottom:-22px;margin-left:-8px;border:8px solid transparent;border-bottom-color:var(--orange)}
.brand{top:-4px;left:458px;width:284px;height:190px;border-radius:50%;background:var(--white);display:flex;flex-direction:column;align-items:center;justify-content:center;z-index:3;border-bottom:4px solid var(--orange)}
.brand .dot{width:46px;height:46px;border-radius:50%;background:var(--orange);margin-bottom:8px}
.brand .name{font-weight:700;font-size:17px;color:var(--ink);text-align:center;line-height:1.2}

/* hero */
.hero{top:115px;left:0;width:1200px;height:645px;background:linear-gradient(180deg,#8fc3e6 0%,#cfe6f2 30%,#e8e2d4 48%,#5fc3c9 65%,#2f9fae 100%)}
.hero h1{top:180px;left:0;width:1200px;font-family:var(--deco);font-weight:400;font-size:38px;color:var(--white);text-align:center;line-height:50px}
.hero p{top:240px;left:250px;width:700px;font-size:15px;font-weight:700;color:var(--white);line-height:22px;text-align:center}
.btn{top:305px;left:527px;width:146px;height:48px;border-radius:24px;background:var(--orange);color:var(--white);font-size:14px;font-weight:700;display:flex;align-items:center;justify-content:center;letter-spacing:.5px}
.arrow-btn{width:56px;height:56px;border-radius:50%;border:2px solid var(--white);background:rgba(255,255,255,.35);display:flex;align-items:center;justify-content:center;top:239px}
.dots{top:458px;left:572px;display:flex;gap:8px}
.dots i{width:12px;height:12px;border-radius:50%;background:var(--white)}
.dots i.on{background:var(--orange)}

/* booking */
.booking{top:758px;left:0;width:1200px;height:450px;background:var(--grey-bg)}
.section-title{font-family:var(--deco);font-weight:400;font-size:28px;color:var(--ink);text-align:center;width:1200px;left:0}
.lead{font-size:14px;line-height:22px;color:var(--text);text-align:center}
.feature{width:250px;text-align:center}
.feature .icon{width:108px;height:108px;border-radius:50%;background:var(--white);box-shadow:0 2px 8px rgba(0,0,0,.15);margin:0 auto;display:flex;align-items:center;justify-content:center}
.feature h3{margin-top:20px;font-size:18px;font-weight:600;color:var(--ink)}
.feature p{margin-top:10px;font-size:14px;line-height:22px;color:var(--muted)}

/* about */
.portrait-ring{top:1304px;left:190px;width:330px;height:330px;border-radius:50%;border:3px solid var(--orange)}
.portrait{top:1318px;left:204px;width:302px;height:302px;border-radius:50%;background:radial-gradient(circle at 50% 45%,#d6a98c 0%,#8a6650 55%,#5d4f45 100%)}
.about-title{top:1300px;left:599px;font-family:var(--deco);font-size:28px;color:var(--ink)}
.about-text{top:1358px;left:597px;width:494px;font-size:14px;line-height:22.4px;color:var(--text)}
.signature{top:1535px;left:599px;width:195px;height:50px;background:linear-gradient(90deg,rgba(240,135,74,.18),rgba(240,135,74,.04));border-radius:4px}
.role{top:1597px;left:600px;font-size:17px;font-weight:700;color:var(--ink)}

/* services */
.cell{width:327px;height:229px}
.text-cell{background:var(--white);text-align:center;padding:32px 20px 0}
.num{width:42px;height:42px;border-radius:50%;background:var(--peach);margin:0 auto;display:flex;align-items:center;justify-content:center;font-weight:700;font-size:17px;color:var(--ink)}
.text-cell h3{margin-top:12px;font-size:19px;font-weight:700;color:var(--ink)}
.text-cell p{margin-top:10px;font-size:14px;line-height:22px;color:var(--text)}

/* testimonial */
.testimonial-bg{top:2340px;left:0;width:1200px;height:620px}
.t-title{top:2462px;color:var(--white)}
.quote-badge{top:2516px;left:578px;width:46px;height:46px;border-radius:50%;background:var(--orange);display:flex;align-items:center;justify-content:center}
.quote{top:2584px;left:250px;width:700px;font-size:14px;font-style:italic;line-height:22.5px;color:var(--white);text-align:center}
.who{top:2698px;left:0;width:1200px;text-align:center;color:var(--white);font-size:17px;font-weight:700;line-height:26px}
.play{top:2763px;left:571px}

/* gallery */
.gal{background:linear-gradient(180deg,#f2b27a,#e08a55 55%,#6fb5c3)}
.gal.b{background:linear-gradient(180deg,#cfd8de,#9ccad6 55%,#3f9fb1)}
.gal.c{background:linear-gradient(180deg,#9b8a70,#c9b08e 55%,#6d5a45)}
.gal.d{background:linear-gradient(180deg,#5b8a7a,#8fb9b0 45%,#5b4630)}
.gal.e{background:linear-gradient(180deg,#4f8fd0,#9ed2e6 45%,#e6d6b5)}

/* footer */
.scene{top:3598px;left:0;width:1200px;height:470px;background:linear-gradient(180deg,#ffffff 0%,#f6efe6 25%,#f3d9bf 45%,#cfe3dc 70%,#b9dde0 100%)}
.consult{top:3640px;left:420px;width:360px;padding:22px 26px;background:rgba(255,255,255,.94);border-top:4px solid var(--orange);border-radius:6px;box-shadow:0 4px 14px rgba(0,0,0,.12)}
.consult h3{font-family:var(--deco);font-weight:400;font-size:20px;color:var(--ink);text-align:center;margin-bottom:14px}
.consult label{display:block;font-size:12px;font-weight:600;color:var(--text);margin-bottom:4px}
.consult input,.consult select{display:block;width:100%;height:32px;border:1px solid #cfcfcf;border-radius:4px;padding:0 10px;font-family:var(--sans);font-size:13px;color:var(--text);background:var(--white);margin-bottom:10px}
.consult button{display:block;width:100%;height:36px;border:0;border-radius:18px;background:var(--orange);color:var(--white);font-family:var(--sans);font-size:13px;font-weight:700;letter-spacing:.5px;margin-top:4px}
.footer{top:3990px;left:0;width:1200px;height:448px}
.subscribe{top:4048px;left:375px;width:451px;height:40px;border-radius:20px;background:var(--white);border:2px solid var(--orange);overflow:hidden}
.subscribe span{position:absolute;left:34px;top:10px;font-size:13px;color:var(--muted)}
.subscribe b{position:absolute;right:0;top:0;width:150px;height:36px;border-radius:18px;background:var(--orange);color:var(--white);font-size:13px;font-weight:700;display:flex;align-items:center;justify-content:center}
.f-head{top:4150px;font-size:21px;font-weight:700;color:var(--white)}
.f-list{list-style:none;font-size:15px;color:var(--white);line-height:28.5px}
.f-contact li{display:flex;gap:14px;align-items:flex-start}
.f-contact svg{margin-top:8px;flex:none}
.f-contact .mail{font-size:13.5px;white-space:nowrap}
.divider{top:4154px;width:1px;height:150px;background:#6b6567}
.social{top:4195px;left:899px;display:flex;gap:8px}
.social i{width:38px;height:38px;border-radius:50%;border:2px solid var(--white);display:block}
.copy{top:4374px;left:0;width:1200px;text-align:center;font-size:14px;color:var(--white)}
</style>
</head>
<body>

<header>
  <div class="abs topbar">
    <span style="left:110px">
      <svg width="13" height="13" viewBox="0 0 24 24"><path fill="#fff" d="M6.6 10.8a15 15 0 0 0 6.6 6.6l2.2-2.2c.3-.3.7-.4 1-.2 1.1.4 2.3.6 3.6.6.6 0 1 .4 1 1V20c0 .6-.4 1-1 1A17 17 0 0 1 3 4c0-.6.4-1 1-1h3.5c.6 0 1 .4 1 1 0 1.3.2 2.5.6 3.6.1.3 0 .7-.2 1z"/></svg>
      Call us Today : +1 555 014 2290
    </span>
    <span style="left:700px">
      <svg width="14" height="11" viewBox="0 0 24 18"><path fill="#fff" d="M0 0h24v2l-12 7L0 2zM0 4l12 7 12-7v14H0z"/></svg>
      Mail : info@harborsandhammocks.example
    </span>
    <span style="left:1043px">
      <svg width="13" height="13" viewBox="0 0 24 24"><circle cx="12" cy="12" r="10" fill="#fff"/><path d="M2 12h20M12 2c3 3 3 17 0 20M12 2c-3 3-3 17 0 20" stroke="#f0874a" stroke-width="1.5" fill="none"/></svg>
      Eng
    </span>
  </div>
  <nav class="abs nav">
    <a class="active" style="left:109px">HOME</a>
    <a style="left:212px">ABOUT US</a>
    <a style="left:348px">SERVICES</a>
    <a style="left:771px">REVIEWS</a>
    <a style="left:898px">CONTACT US</a>
    <svg class="abs" style="left:1073px;top:33px" width="14" height="14" viewBox="0 0 24 24"><circle cx="10" cy="10" r="7" stroke="#f0874a" stroke-width="3" fill="none"/><path d="M15 15l7 7" stroke="#f0874a" stroke-width="3"/></svg>
  </nav>
  <div class="abs brand">
    <div class="dot"></div>
    <div class="name">Harbors &amp; Hammocks<br>Travel Agency</div>
  </div>
</header>

<section class="abs hero" role="img" aria-label="Couple walking along a wooden pier toward a tropical island with turquoise water">
  <h1 class="abs">HARBORS AND HAMMOCKS</h1>
  <p class="abs">Lorem ipsum dolor sit amet, consectetur adipiscing elit, sed do eiusmod tempor incididunt ut labore et dolore magna aliqua. Ut enim ad minim</p>
  <div class="abs btn">BOOK NOW</div>
  <div class="abs arrow-btn" style="left:27px"><svg width="14" height="20" viewBox="0 0 14 20"><path d="M11 2L3 10l8 8" stroke="#333" stroke-width="2.5" fill="none"/></svg></div>
  <div class="abs arrow-btn" style="left:1117px"><svg width="14" height="20" viewBox="0 0 14 20"><path d="M3 2l8 8-8 8" stroke="#333" stroke-width="2.5" fill="none"/></svg></div>
  <div class="abs dots"><i></i><i class="on"></i><i></i></div>
</section>
<svg class="abs" style="top:600px;left:0" width="1200" height="162" viewBox="0 0 1200 162">
  <path d="M0 158 Q600 -40 1200 158 V162 H0 Z" fill="#efefef"/>
  <path d="M0 140 Q600 -58 1200 140" stroke="#f0874a" stroke-width="5" fill="none"/>
</svg>

<section class="abs booking">
  <h2 class="abs section-title" style="top:10px">BOOKING LUXURY VACATIONS</h2>
  <p class="abs lead" style="top:56px;left:300px;width:600px">Lorem ipsum dolor sit amet, consectetur adipiscing elit, sed do eiusmod tempor incididunt ut labore et dolore magna aliqua.</p>
  <div class="abs feature" style="top:126px;left:199px">
    <div class="icon"><svg width="54" height="54" viewBox="0 0 54 54" fill="none" stroke="#f0874a" stroke-width="2"><rect x="4" y="8" width="40" height="36" rx="3"/><path d="M4 17h40M13 4v8M35 4v8"/><path d="M11 23h5M20 23h5M29 23h5M11 30h5M20 30h5M11 37h5"/><circle cx="42" cy="42" r="9" fill="#fff"/><path d="M42 37v5l3 2"/></svg></div>
    <h3>Eiusmod tempor</h3>
    <p>Lorem ipsum dolor sit amet, con se ctetur adipiscing elit, sed do eiusmod tempor</p>
  </div>
  <div class="abs feature" style="top:126px;left:471px">
    <div class="icon"><svg width="54" height="54" viewBox="0 0 54 54" fill="none" stroke="#f0874a" stroke-width="2"><path d="M8 48V22l19-10 19 10v26z"/><path d="M4 48h46M15 28h6M27 28h6M15 36h6M27 36h6M23 48v-7h8v7"/></svg></div>
    <h3>Eiusmod tempor</h3>
    <p>Lorem ipsum dolor sit amet, con se ctetur adipiscing elit, sed do eiusmod tempor</p>
  </div>
  <div class="abs feature" style="top:126px;left:743px">
    <div class="icon"><svg width="54" height="54" viewBox="0 0 54 54" fill="none" stroke="#f0874a" stroke-width="2"><rect x="12" y="4" width="26" height="44" rx="3"/><path d="M21 9h8M23 43h4"/><rect x="17" y="15" width="16" height="14"/><path d="M20 22l4 3 6-6"/></svg></div>
    <h3>Eiusmod tempor</h3>
    <p>Lorem ipsum dolor sit amet, con se ctetur adipiscing elit, sed do eiusmod tempor</p>
  </div>
</section>

<section class="about">
  <div class="abs portrait-ring"></div>
  <div class="abs portrait" role="img" aria-label="Portrait of agency owner Marla Denholm"></div>
  <h2 class="abs about-title">ABOUT "MARLA DENHOLM"</h2>
  <p class="abs about-text">Lorem ipsum dolor sit amet, consectetur adipiscing elit, sed do eiusmod tempor incididunt ut labore et dolore magna aliqua. Ut enim ad minim veniam, quis nostrud exercitation ullamco laboris nisi ut aliquip ex ea commodo consequat. Duis aute irure dolor in reprehenderit in voluptate velit esse cillum dolore eu fugiat nulla pariatur. Excepteur sint occaecat cupidatat non proident, sunt in culpa qui officia deserunt mollit anim id est laborum.</p>
  <div class="abs signature" role="img" aria-label="Handwritten signature of Marla Denholm"></div>
  <div class="abs role">Agency Owner</div>
</section>

<section class="services">
  <h2 class="abs section-title" style="top:1728px">OUR SERVICES</h2>
  <div class="abs cell" style="top:1806px;left:110px;background:linear-gradient(180deg,#c98a5a,#f2c07a 40%,#5a4535 100%)" role="img" aria-label="Two loungers on a deck facing a palm-lined sunset"></div>
  <div class="abs cell text-cell" style="top:1806px;left:437px">
    <div class="num">02</div>
    <h3>Lorem ipsum dolor sit</h3>
    <p>Lorem ipsum dolor sit amet, consectetur adipiscing elit, sed do eiusmod tempor incididunt ut labore et dolore</p>
  </div>
  <div class="abs cell" style="top:1806px;left:764px;background:linear-gradient(180deg,#e9ecea,#bcc7bd 45%,#3fb3c2 100%)" role="img" aria-label="Modern villa with a private pool and garden"></div>
  <div class="abs cell text-cell" style="top:2035px;left:110px">
    <div class="num">01</div>
    <h3>Lorem ipsum dolor sit</h3>
    <p>Lorem ipsum dolor sit amet, consectetur adipiscing elit, sed do eiusmod tempor incididunt ut labore et dolore</p>
  </div>
  <div class="abs cell" style="top:2035px;left:437px;background:linear-gradient(180deg,#cfe3ef,#8fb08a 40%,#ece6dc 100%)" role="img" aria-label="Traveller walking along a white sand beach path"></div>
  <div class="abs cell text-cell" style="top:2035px;left:764px">
    <div class="num">03</div>
    <h3>Lorem ipsum dolor sit</h3>
    <p>Lorem ipsum dolor sit amet, consectetur adipiscing elit, sed do eiusmod tempor incididunt ut labore et dolore</p>
  </div>
</section>

<section class="testimonial">
  <svg class="abs testimonial-bg" viewBox="0 0 1200 620" role="img" aria-label="Couple seated on a beach at dusk among lanterns and tents">
    <defs>
      <linearGradient id="dusk" x1="0" y1="0" x2="0" y2="1">
        <stop offset="0" stop-color="#3c4150"/>
        <stop offset=".45" stop-color="#5a5560"/>
        <stop offset=".75" stop-color="#7a6048"/>
        <stop offset="1" stop-color="#a07a52"/>
      </linearGradient>
    </defs>
    <path d="M0 131 Q600 -77 1200 131 V466 Q600 674 0 466 Z" fill="url(#dusk)"/>
    <path d="M0 110 Q600 -98 1200 110" stroke="#f0874a" stroke-width="5" fill="none"/>
    <path d="M0 490 Q600 698 1200 490" stroke="#f0874a" stroke-width="5" fill="none"/>
  </svg>
  <h2 class="abs section-title t-title">WHAT PEOPLE ARE SAYING</h2>
  <div class="abs quote-badge"><svg width="20" height="16" viewBox="0 0 20 16"><path fill="#fff" d="M0 16V9C0 4 2 1 7 0v3C4 4 4 6 4 8h4v8zM11 16V9c0-5 2-8 7-9v3c-3 1-3 3-3 5h4v8z"/></svg></div>
  <svg class="abs" style="top:2612px;left:46px" width="26" height="54" viewBox="0 0 26 54"><path d="M24 2L2 27l22 25" stroke="#fff" stroke-width="2.5" fill="none"/></svg>
  <svg class="abs" style="top:2612px;left:1128px" width="26" height="54" viewBox="0 0 26 54"><path d="M2 2l22 25L2 52" stroke="#fff" stroke-width="2.5" fill="none"/></svg>
  <p class="abs quote">“Lorem ipsum dolor sit amet, consectetur adipiscing elit, sed do eiusmod tempor incididunt ut labore et dolore magna aliqua. Ut enim ad minim veniam, quis nostrud exercitation ullamco laboris nisi ut aliquip ex ea commodo consequat. Duis aute irure dolor in reprehenderit in voluptate velit esse cillum dolore eu fugiat nulla pariatur. Excepteur sint occaecat cupidatat non proident, sunt in culpa</p>
  <div class="abs who">John Doe<br>Company name</div>
  <svg class="abs play" width="54" height="54" viewBox="0 0 54 54"><circle cx="27" cy="27" r="24" stroke="#fff" stroke-width="4" fill="none"/><path d="M21 16l16 11-16 11z" fill="#fff"/></svg>
</section>

<section class="gallery">
  <h2 class="abs section-title" style="top:3008px">OUR GALLEY</h2>
  <div class="abs gal" style="top:3080px;left:110px;width:483px;height:238px" role="img" aria-label="Couple relaxing in an infinity pool at sunset"></div>
  <div class="abs gal b" style="top:3080px;left:604px;width:483px;height:238px" role="img" aria-label="Friends jumping into a sea-edge pool"></div>
  <div class="abs gal c" style="top:3328px;left:110px;width:319px;height:238px" role="img" aria-label="Couple resting in a wooden boat on the shore"></div>
  <div class="abs gal d" style="top:3328px;left:441px;width:318px;height:238px" role="img" aria-label="Couple on a deck overlooking limestone islands"></div>
  <div class="abs gal e" style="top:3328px;left:770px;width:318px;height:238px" role="img" aria-label="Two beach chairs under a bright sky"></div>
</section>

<footer>
  <div class="abs scene" role="img" aria-label="Faded tropical shoreline with a sunset travel illustration"></div>

  <form class="abs consult" action="mailto:marla@harborsandhammockstravel.example" method="post" enctype="text/plain">
    <h3>FREE CONSULTATION</h3>
    <label for="c-name">Your name</label>
    <input id="c-name" name="name" type="text">
    <label for="c-email">Email address</label>
    <input id="c-email" name="email" type="email">
    <label for="c-dest">Dream destination</label>
    <select id="c-dest" name="destination">
      <option>Hawaii</option><option>Europe</option><option>Caribbean</option><option>Other</option>
    </select>
    <button type="submit">REQUEST CONSULTATION</button>
  </form>

  <svg class="abs footer" viewBox="0 0 1200 448" preserveAspectRatio="none">
    <path d="M0 70 Q600 -60 1200 70 V448 H0 Z" fill="#2b2627"/>
    <path d="M0 62 Q600 -68 1200 62" stroke="#7fc6cf" stroke-width="3" fill="none"/>
  </svg>
  <div class="abs subscribe"><span>Email address</span><b>SUBSCRIBE</b></div>

  <h4 class="abs f-head" style="left:138px">Links</h4>
  <ul class="abs f-list" style="top:4194px;left:139px">
    <li>Home</li><li>Services</li><li>Blog</li><li>Contact</li>
  </ul>
  <div class="abs divider" style="left:336px"></div>

  <h4 class="abs f-head" style="left:461px">Contact us</h4>
  <ul class="abs f-list f-contact" style="top:4194px;left:461px;width:350px">
    <li><svg width="11" height="14" viewBox="0 0 12 16"><path fill="#f0874a" d="M6 0a6 6 0 0 1 6 6c0 4-6 10-6 10S0 10 0 6a6 6 0 0 1 6-6zm0 4a2 2 0 1 0 0 4 2 2 0 0 0 0-4z"/></svg><span>123,Lorem ipsum dolor sit amet,<br>consec</span></li>
    <li><svg width="12" height="12" viewBox="0 0 24 24"><path fill="#f0874a" d="M6.6 10.8a15 15 0 0 0 6.6 6.6l2.2-2.2c.3-.3.7-.4 1-.2 1.1.4 2.3.6 3.6.6.6 0 1 .4 1 1V20c0 .6-.4 1-1 1A17 17 0 0 1 3 4c0-.6.4-1 1-1h3.5c.6 0 1 .4 1 1 0 1.3.2 2.5.6 3.6.1.3 0 .7-.2 1z"/></svg><span>+1 555 014 2290</span></li>
    <li><svg width="13" height="10" viewBox="0 0 24 18"><path fill="#f0874a" d="M0 0h24v2l-12 7L0 2zM0 4l12 7 12-7v14H0z"/></svg><span class="mail">marla@harborsandhammockstravel.example</span></li>
  </ul>
  <div class="abs divider" style="left:818px"></div>

  <h4 class="abs f-head" style="left:943px">Follow us</h4>
  <div class="abs social"><i aria-label="Social link 1"></i><i aria-label="Social link 2"></i><i aria-label="Social link 3"></i><i aria-label="Social link 4"></i></div>

  <p class="abs copy">© Copyrights.2021.The Company Name.All Rights Reserved</p>
</footer>

</body>
</html>
```